Venna coffee business card

a business card for a cofee van business

similar to the sample business card i am sending
front side with lighter back ground (milky colo or light creamr)
instead of cup please insert my logo
details of business:
email, facebook mobile number (larger fonts)

The back of business card
the bacground is white

the van photo(attached)

this text should be printed (enhance your events with a great coffeevan)

```html
<!DOCTYPE html>
<html lang="en">
<head>
<meta charset="utf-8">
<title>Venna Mobile Café – Business Card</title>
<link rel="stylesheet" href="https://fonts.googleapis.com/css2?family=Arimo:wght@400;700&family=Italianno&display=swap">
<style>
  :root {
    --page-bg: #e9e6e2;
    --card-cream: #f4efe7;
    --card-cream-deep: #e8dfd2;
    --card-white: #ffffff;
    --espresso: #3b1f16;
    --roast: #5a2f22;
    --caramel: #a8754f;
    --bean-light: #c9ad95;
    --bean-dark: #7a5440;
    --ink: #1c1c1c;
    --van-brown: #8a5638;
    --van-light: #c9a27f;
    --shadow: rgba(40, 25, 15, 0.18);
  }
  * { box-sizing: border-box; margin: 0; padding: 0; }
  html, body {
    width: 1200px; height: 844px; overflow: hidden;
    background: var(--page-bg);
  }
  .canvas {
    position: relative; width: 1200px; height: 844px;
    display: flex; align-items: center; justify-content: center; gap: 60px;
  }
  .card {
    position: relative; width: 510px; height: 292px;
    box-shadow: 0 10px 24px var(--shadow);
    overflow: hidden;
  }

  /* Front */
  .card--front {
    background: linear-gradient(100deg, var(--card-cream-deep) 0%, var(--card-cream) 45%, #f8f4ee 100%);
  }
  .card__beans {
    position: absolute; left: 0; bottom: 0; width: 235px; height: 250px;
    background: radial-gradient(ellipse at 40% 60%, var(--bean-dark) 0%, var(--bean-light) 55%, rgba(244,239,231,0) 78%);
    opacity: 0.85;
  }
  .brand {
    position: absolute; left: 255px; top: 22px; width: 220px;
    display: flex; flex-direction: column; align-items: center; gap: 8px;
  }
  .brand__mark {
    width: 62px; height: 62px; border-radius: 50%;
    background: var(--caramel);
  }
  .brand__name {
    font-family: "Arimo", sans-serif; font-weight: 700; font-size: 17px;
    color: var(--roast); letter-spacing: 0.3px;
  }
  .holder {
    position: absolute; left: 262px; top: 128px;
    font-family: "Italianno", cursive; font-size: 44px; line-height: 1;
    color: var(--espresso);
  }
  .contacts {
    position: absolute; left: 262px; top: 182px;
    list-style: none; display: flex; flex-direction: column; gap: 6px;
    font-family: "Arimo", sans-serif; font-size: 17px; color: var(--ink);
  }
  .contacts__item { display: flex; align-items: center; gap: 8px; }
  .contacts__icon { width: 14px; height: 14px; flex: none; fill: var(--espresso); }
  .contacts__square { width: 11px; height: 11px; background: var(--espresso); flex: none; margin: 0 1px 0 2px; }

  /* Back */
  .card--back { background: var(--card-white); }
  .card__van {
    position: absolute; left: 28px; top: 40px; width: 260px; height: 225px;
    border-radius: 18px;
    background: linear-gradient(180deg, var(--van-light) 0%, var(--van-brown) 70%, var(--roast) 100%);
  }
  .tagline {
    position: absolute; left: 300px; top: 138px; width: 190px;
    font-family: "Arimo", sans-serif; font-size: 15px; line-height: 1.3;
    color: var(--ink); text-align: center;
  }
</style>
</head>
<body>
<main class="canvas">
  <section class="card card--front" aria-label="Business card front">
    <div class="card__beans" role="img" aria-label="Roasted coffee beans photograph fading into the cream background"></div>
    <div class="brand">
      <span class="brand__mark" aria-hidden="true"></span>
      <span class="brand__name">Venna Mobile Café</span>
    </div>
    <p class="holder">Marco Bell</p>
    <ul class="contacts">
      <li class="contacts__item">
        <svg class="contacts__icon" viewBox="0 0 24 24" aria-hidden="true"><path d="M6.6 10.8a15 15 0 0 0 6.6 6.6l2.2-2.2a1 1 0 0 1 1-.25 11.4 11.4 0 0 0 3.6.57 1 1 0 0 1 1 1V20a1 1 0 0 1-1 1A17 17 0 0 1 3 4a1 1 0 0 1 1-1h3.5a1 1 0 0 1 1 1c0 1.25.2 2.45.57 3.57a1 1 0 0 1-.25 1z"/></svg>
        <span>444 555 0192</span>
      </li>
      <li class="contacts__item">
        <svg class="contacts__icon" viewBox="0 0 24 24" aria-hidden="true"><path d="M2 5h20v14H2z M4 7v.5l8 5 8-5V7l-8 5z" fill-rule="evenodd"/></svg>
        <span>info@vennacafe.com</span>
      </li>
      <li class="contacts__item">
        <span class="contacts__square" aria-hidden="true"></span>
        <span>www.vennacafe.com/page</span>
      </li>
    </ul>
  </section>

  <section class="card card--back" aria-label="Business card back">
    <div class="card__van" role="img" aria-label="Illustration of a brown coffee van with a steaming cup on its roof"></div>
    <p class="tagline">Enhance your events<br>with a great coffeevan</p>
  </section>
</main>
</body>
</html>
```